Responsive Software/Service company website

I need a complete, responsive, company website design (Wordpress).
A short intro to what we do:
Corvalink is a Danish software company specialized in Brightwell Ledger ORB for SMB clients in Europe.
We deliver POS and ERP systems to retail shops and entertainment business.
Besides this, we offer tight integration to eCommerce solutions.
For eCommerce we have 2 products, both heavily customized for a tight integration.
B2C (Pellucid) and B2B
For both eCommerce and ORB solutions we have several sub groups, modules and specifications.
Our target group is existing (looking for eCommerce) and new retailers (looking for POS and eCommerce)
I'm looking for a clean way to promote our products in an easily accessible way.
As well as having a section for more detailed information on each product.
I have uploaded a wire frame suggestion. Please do not take it too literally. You have absolutely creative freedom if you have a better, more creative idea.
See it as an inspiration as to what elements we would like on the site (not necessarily on the front page)
Feel free to use/suggest Stock photos. We are aware that prices of those come on top. We also have pro photographer+studio available if you have any suggestions that requires that.
Updates
Hi all
Target Market(s)
European retailers/shop owners.
Either looking for a POS / ERP system or looking for eCommerce integration to their existing BW ORB system.
Industry/Entity Type
Entertainment
Requirements
Must have
- The logo I uploaded has to be part of it. Can't be changed.
Same goes for colours
Must be responsive to work on mobile and desktop. Final design PSDs must reflect this and show how it would look on both platforms.
Final PSds must also show examples of any interaction like mouseover, colour changes, image change or dynamics.
Nice to have
- Custom made icons to accompany(replace?) text links are a very big plus.
Custom made icons/logo for each sub product (see wire frame bottom) :
CL Retail
CL Entertainment
CL Ticketing
CL Webshop
etc
for easily distinction would be a big plus too.
The use of "hand drawn" elements mixed with straight, minimalistic design, like here on ArtHarbor, can be used.
Should not have
- This is the existing site I'm looking to change away from:
http://www.corvalink-example.dk/ (in danish)
Too much info, too cramped, not nice looking and generally not very user friendly imo.

```html
<!DOCTYPE html>
<html lang="en">
<head>
<meta charset="utf-8">
<title>Corvalink – Mobile Home</title>
<link rel="stylesheet" href="https://fonts.googleapis.com/css2?family=Questrial&family=Open+Sans:wght@400&display=swap">
<style>
  :root {
    --bar-top: #2a2a2a;
    --bar-bottom: #0c0c0c;
    --brand-blue: #2b6cb8;
    --accent-blue: #4b93d6;
    --search-grey: #3b3b3b;
    --stage-light: #8a8a8a;
    --stage-mid: #5a5a5a;
    --stage-dark: #2e2e2e;
    --text-white: #ffffff;
    --text-body: #444444;
    --rule: rgba(255,255,255,0.55);
  }
  * { box-sizing: border-box; margin: 0; padding: 0; }
  html, body { width: 768px; height: 1200px; overflow: hidden; }
  body {
    font-family: "Open Sans", sans-serif;
    background:
      radial-gradient(ellipse 70% 45% at 30% 30%, rgba(190,190,190,0.45), transparent 70%),
      radial-gradient(ellipse 60% 40% at 75% 70%, rgba(150,150,150,0.35), transparent 70%),
      linear-gradient(180deg, var(--stage-mid) 0%, var(--stage-light) 30%, var(--stage-mid) 65%, var(--stage-dark) 100%);
    position: relative;
  }
  .site-header {
    position: absolute; top: 0; left: 0; width: 768px;
    height: 76px;
    display: flex;
    align-items: stretch;
    background: linear-gradient(180deg, var(--bar-top), var(--bar-bottom));
  }
  .menu-toggle { width: 76px; display: flex; align-items: center; justify-content: center; }
  .brand {
    flex: 1; display: flex; align-items: center; justify-content: center;
    font-family: "Questrial", sans-serif; font-size: 34px; letter-spacing: 2px;
    color: var(--brand-blue); text-transform: uppercase; padding-top: 4px;
  }
  .search-btn { width: 74px; background: var(--search-grey); display: flex; align-items: center; justify-content: center; }
  .download-btn { width: 72px; background: var(--accent-blue); display: flex; align-items: center; justify-content: center; }
  .hero-heading {
    position: absolute; top: 130px; left: 0; width: 768px; text-align: center;
    font-family: "Questrial", sans-serif; font-weight: 400;
    font-size: 46px; letter-spacing: -1px; color: var(--text-white); line-height: 60px;
  }
  .heading-rule {
    position: absolute; top: 211px; left: 69px; width: 630px; height: 8px;
    display: flex; align-items: center; gap: 8px;
  }
  .heading-rule .line { flex: 1; border-top: 1px dashed var(--rule); }
  .heading-rule .hatch {
    width: 68px; height: 8px;
    background: repeating-linear-gradient(90deg, var(--rule) 0 1px, transparent 1px 3px);
  }
  .product-card { position: absolute; left: 192px; width: 384px; height: 408px; }
  .product-card.retail { top: 250px; }
  .product-card.webshop { top: 680px; }
  .card-title { font-family: "Questrial", sans-serif; font-size: 20px; fill: var(--text-white); }
  .card-text { font-family: "Open Sans", sans-serif; font-size: 14px; fill: var(--text-body); }
  .scroll-down {
    position: absolute; left: 344px; top: 1106px;
    width: 80px; height: 80px; border-radius: 50%;
    background: rgba(40,40,40,0.85);
    display: flex; align-items: center; justify-content: center;
  }
</style>
</head>
<body>
  <header class="site-header">
    <div class="menu-toggle">
      <svg width="46" height="32" viewBox="0 0 46 32" aria-label="Menu">
        <g stroke="#fff" stroke-width="2.5">
          <line x1="2" y1="4" x2="44" y2="4"/><line x1="2" y1="12" x2="44" y2="12"/>
          <line x1="2" y1="20" x2="44" y2="20"/><line x1="2" y1="28" x2="30" y2="28"/>
        </g>
      </svg>
    </div>
    <div class="brand">Corvalink</div>
    <div class="search-btn">
      <svg width="30" height="30" viewBox="0 0 30 30" aria-label="Search">
        <circle cx="12" cy="12" r="8" fill="none" stroke="#ddd" stroke-width="2.5"/>
        <line x1="18" y1="18" x2="27" y2="27" stroke="#ddd" stroke-width="3"/>
      </svg>
    </div>
    <div class="download-btn">
      <svg width="24" height="24" viewBox="0 0 24 24" aria-label="Download">
        <path d="M8 3h8v8h5l-9 10-9-10h5z" fill="#fff"/>
      </svg>
    </div>
  </header>

  <h1 class="hero-heading">LOREM IPSUM HEADING</h1>
  <div class="heading-rule"><span class="line"></span><span class="hatch"></span><span class="line"></span></div>

  <svg class="product-card retail" viewBox="0 0 240 255">
    <defs>
      <clipPath id="blob-retail">
        <path d="M120 2 C140 2 150 12 158 20 C175 14 205 18 222 38 C238 56 240 80 238 100 L238 160 C240 200 220 225 190 232 C170 236 160 240 150 246 C135 256 105 256 90 246 C80 240 70 236 50 232 C20 225 0 200 2 160 L2 100 C0 80 2 56 18 38 C35 18 65 14 82 20 C90 12 100 2 120 2 Z"/>
      </clipPath>
      <linearGradient id="photo-retail" x1="0" y1="0" x2="1" y2="1">
        <stop offset="0" stop-color="#c9a07a"/><stop offset="0.5" stop-color="#6b8fc0"/><stop offset="1" stop-color="#7a3a3a"/>
      </linearGradient>
    </defs>
    <g clip-path="url(#blob-retail)">
      <rect width="240" height="255" fill="#fff"/>
      <rect width="240" height="160" fill="url(#photo-retail)" role="img" aria-label="Shop assistant and cashier smiling at a store checkout"/>
      <rect y="134" width="240" height="26" fill="rgba(0,0,0,0.78)"/>
    </g>
    <text class="card-title" x="120" y="154" text-anchor="middle">Retail</text>
    <text class="card-text" x="120" y="188" text-anchor="middle">Solutions for</text>
    <text class="card-text" x="120" y="209" text-anchor="middle">all industies</text>
  </svg>

  <svg class="product-card webshop" viewBox="0 0 240 255">
    <defs>
      <clipPath id="blob-webshop">
        <path d="M120 2 C140 2 150 12 158 20 C175 14 205 18 222 38 C238 56 240 80 238 100 L238 160 C240 200 220 225 190 232 C170 236 160 240 150 246 C135 256 105 256 90 246 C80 240 70 236 50 232 C20 225 0 200 2 160 L2 100 C0 80 2 56 18 38 C35 18 65 14 82 20 C90 12 100 2 120 2 Z"/>
      </clipPath>
      <linearGradient id="photo-webshop" x1="0" y1="0" x2="1" y2="1">
        <stop offset="0" stop-color="#8a9a4a"/><stop offset="0.45" stop-color="#e8cfc0"/><stop offset="1" stop-color="#2a2a2a"/>
      </linearGradient>
    </defs>
    <g clip-path="url(#blob-webshop)">
      <rect width="240" height="255" fill="#fff"/>
      <rect width="240" height="160" fill="url(#photo-webshop)" role="img" aria-label="Hands holding a payment card above a laptop keyboard"/>
      <rect y="134" width="240" height="26" fill="rgba(0,0,0,0.85)"/>
    </g>
    <text class="card-title" x="120" y="154" text-anchor="middle">Webshop</text>
    <text class="card-text" x="120" y="188" text-anchor="middle">E-commerce</text>
    <text class="card-text" x="120" y="209" text-anchor="middle">from ORB</text>
  </svg>

  <div class="scroll-down">
    <svg width="26" height="26" viewBox="0 0 24 24" aria-label="Scroll down">
      <path d="M9 4h6v7h4l-7 8-7-8h4z" fill="#cfcfcf"/>
    </svg>
  </div>
</body>
</html>
```